Business Card Admin Services

I have just selected a new logo. Now I need a business card.

The business is contract administrative services. We provide high value administrative services to small businesses/offices. We are professional, efficient, but also have fun and energetic personalities.

Lora Pike
Lora@DeskFalcon.ca
604-913-4078
DeskFalcon.ca

I will also want Facebook, Twitter and LinkedIn icons on the card - please up my "handles" beside each.
Facebook is DeskFalconCanada
Twitter is @DFalconLora
LinkedIn is LoraPikeDeskFalcon
Updates

New logo just updated.  Thanks for your patience!

Target Market(s)

Small businesses, professional offices

Industry/Entity Type

Business

Requirements
Must have
• bold, fun use of my colours
font needs to be consistent with the logo
Nice to have
• I quite like a closeup of the head

```html
<!DOCTYPE html>
<html lang="en">
<head>
<meta charset="utf-8">
<title>DeskFalcon Business Card</title>
<link rel="stylesheet" href="https://fonts.googleapis.com/css2?family=Questrial&display=swap">
<style>
  :root {
    --brand-pink: #ec1e80;
    --stage-pink: #e6459a;
    --stage-pink-light: #ea6aa9;
    --ink: #0d0d0d;
    --paper: #ffffff;
    --paper-soft: #f7f7f7;
  }
  * { margin: 0; padding: 0; box-sizing: border-box; }
  html, body {
    width: 1200px; height: 1000px; overflow: hidden;
  }
  body {
    position: relative;
    font-family: "Questrial", "Helvetica Neue", Arial, sans-serif;
    background: radial-gradient(ellipse at 50% 55%, var(--stage-pink-light) 0%, var(--stage-pink) 60%, var(--brand-pink) 100%);
    color: var(--paper);
  }
  .sheet-title, .side-label {
    position: absolute;
    font-size: 44px;
    letter-spacing: 0.5px;
    color: var(--paper);
    line-height: 1;
  }
  .sheet-title { left: 28px; top: 32px; }
  .side-label--front { left: 24px; top: 584px; }
  .side-label--back { left: 597px; top: 584px; }

  .card {
    position: absolute;
    top: 637px;
    width: 555px;
    height: 341px;
    overflow: hidden;
  }

  /* Front */
  .card--front {
    left: 24px;
    background: linear-gradient(180deg, var(--paper) 0%, var(--paper-soft) 80%, #f6c9dd 89%, var(--brand-pink) 100%);
  }
  .front-mark {
    position: absolute;
    left: 246px; top: 98px;
    width: 70px; height: 70px;
    border-radius: 50%;
    background: var(--brand-pink);
  }
  .front-name {
    position: absolute;
    left: 0; right: 0; top: 188px;
    text-align: center;
    font-size: 28px;
    letter-spacing: 0.5px;
    color: var(--brand-pink);
  }

  /* Back */
  .card--back {
    left: 596px;
    background: var(--brand-pink);
  }
  .back-splash {
    position: absolute; left: 0; top: 0;
    width: 555px; height: 341px;
  }
  .back-mark {
    position: absolute;
    left: 320px; top: 68px;
    width: 180px; height: 180px;
    border-radius: 50%;
    border: 6px solid var(--paper);
  }
  .back-brand {
    position: absolute;
    left: 310px; width: 200px; top: 255px;
    text-align: center;
    font-size: 24px;
    letter-spacing: 0.5px;
    color: var(--paper);
  }
  .holder-name {
    position: absolute;
    left: 32px; top: 44px;
    font-size: 30px;
    letter-spacing: 0.5px;
    color: var(--paper);
  }
  .holder-name .surname { color: var(--ink); }
  .contact-list {
    position: absolute;
    left: 32px; top: 94px;
    list-style: none;
  }
  .contact-item {
    display: flex; align-items: center;
    height: 33.4px;
    font-size: 14px;
    letter-spacing: 0.6px;
    text-transform: uppercase;
    color: var(--paper);
  }
  .contact-icon {
    width: 25px; height: 25px;
    margin-right: 14px;
    border-radius: 4px;
    background: var(--ink);
    display: flex; align-items: center; justify-content: center;
    flex: none;
  }
</style>
</head>
<body>
  <h1 class="sheet-title">BUSINESS CARD</h1>

  <p class="side-label side-label--front">FRONT</p>
  <section class="card card--front" aria-label="Card front">
    <div class="front-mark"></div>
    <p class="front-name">DESKFALCON</p>
  </section>

  <p class="side-label side-label--back">BACK</p>
  <section class="card card--back" aria-label="Card back">
    <svg class="back-splash" viewBox="0 0 555 341" role="img" aria-label="Black brush-stroke splash panel behind the brand mark">
      <polygon fill="#0d0d0d" points="345,0 555,0 555,341 230,341 235,300 245,250 255,190 270,130 290,70 315,25"/>
    </svg>
    <div class="back-mark"></div>
    <p class="back-brand">DESKFALCON</p>

    <h2 class="holder-name">LORA <span class="surname">PIKE</span></h2>
    <ul class="contact-list">
      <li class="contact-item">
        <span class="contact-icon">
          <svg width="17" height="12" viewBox="0 0 17 12"><rect x="0.75" y="0.75" width="15.5" height="10.5" fill="none" stroke="#fff" stroke-width="1.5"/><polyline points="1,1 8.5,7 16,1" fill="none" stroke="#fff" stroke-width="1.5"/></svg>
        </span>Lora@DeskFalcon.ca
      </li>
      <li class="contact-item">
        <span class="contact-icon">
          <svg width="15" height="15" viewBox="0 0 24 24"><path fill="#fff" d="M6.6 10.8a15.1 15.1 0 0 0 6.6 6.6l2.2-2.2a1 1 0 0 1 1-.25 11.4 11.4 0 0 0 3.6.57 1 1 0 0 1 1 1V20a1 1 0 0 1-1 1A17 17 0 0 1 3 4a1 1 0 0 1 1-1h3.5a1 1 0 0 1 1 1c0 1.25.2 2.45.57 3.57a1 1 0 0 1-.25 1z"/></svg>
        </span>604-913-4078
      </li>
      <li class="contact-item">
        <span class="contact-icon">
          <svg width="16" height="16" viewBox="0 0 16 16" fill="none" stroke="#fff" stroke-width="1.2"><circle cx="8" cy="8" r="7"/><ellipse cx="8" cy="8" rx="3" ry="7"/><line x1="1" y1="8" x2="15" y2="8"/><line x1="2.2" y1="4.5" x2="13.8" y2="4.5"/><line x1="2.2" y1="11.5" x2="13.8" y2="11.5"/></svg>
        </span>DeskFalcon.ca
      </li>
      <li class="contact-item"><span class="contact-icon"></span>DeskFalconCanada</li>
      <li class="contact-item"><span class="contact-icon"></span>@DFalconLora</li>
      <li class="contact-item"><span class="contact-icon"></span>LoraPikeDeskFalcon</li>
    </ul>
  </section>
</body>
</html>
```